Business Card for innovative, tech/consultant company

We are specializing in bringing together Efficiency methodology and Technology for our Business customers. We would like an astonishing business Card that matches this idea.

Target Market(s)

Businesses of medium size or more

Industry/Entity Type

Business Consultant

Contact Information for Business Card

Name, Title, personal email, www, address, phone

Font styles to use
Sans Serif

Colors
3277b5

Requirements
Must have
• - innovative, efficient design
• - good readable
• - Colors must match our logo (blue and grey)
• - the attached font (is licensed by our Company) must be used (Syntax LT)
Should not have
• overloaded

```html
<!DOCTYPE html>
<html lang="en">
<head>
<meta charset="utf-8">
<title>Veralink Business Card</title>
<link rel="stylesheet" href="https://fonts.googleapis.com/css2?family=Open+Sans:wght@400;600&display=swap">
<style>
  :root {
    --page-bg: #e6e6e8;
    --card-white: #ffffff;
    --brand-grey: #a7a7ab;
    --text-grey: #8d8d92;
    --wave-grey: #a9a9ae;
    --wave-grey-dark: #96969b;
    --brand-blue: #1a98d5;
  }
  html, body {
    margin: 0;
    width: 1200px;
    height: 780px;
    overflow: hidden;
    background: var(--page-bg);
    font-family: "Open Sans", sans-serif;
  }
  .card {
    position: absolute;
    left: 75px;
    top: 90px;
    width: 1050px;
    height: 600px;
    background: var(--card-white);
    box-shadow: 0 10px 30px rgba(0,0,0,0.18);
    overflow: hidden;
  }
  .card-wave {
    position: absolute;
    inset: 0;
  }
  .card-content {
    position: absolute;
    right: 64px;
    top: 40px;
    text-align: right;
  }
  .brand-name {
    margin: 0;
    font-size: 120px;
    font-weight: 400;
    letter-spacing: -2px;
    line-height: 1;
    color: var(--brand-grey);
  }
  .person-name {
    margin: 18px 0 0;
    font-size: 40px;
    font-weight: 600;
    color: var(--text-grey);
    line-height: 1.1;
  }
  .person-title {
    margin: 2px 0 0;
    font-size: 26px;
    font-weight: 400;
    color: var(--brand-blue);
  }
  .contact-list {
    list-style: none;
    margin: 26px 0 0;
    padding: 0;
  }
  .contact-item {
    display: flex;
    justify-content: flex-end;
    align-items: center;
    gap: 14px;
    font-size: 22px;
    color: var(--text-grey);
    height: 38px;
  }
  .contact-icon {
    width: 28px;
    height: 28px;
    flex: none;
  }
</style>
</head>
<body>
  <main class="card">
    <svg class="card-wave" width="1050" height="600" viewBox="0 0 1050 600" aria-hidden="true">
      <defs>
        <linearGradient id="waveGrey" x1="0" y1="0" x2="0" y2="1">
          <stop offset="0" stop-color="#b3b3b8"/>
          <stop offset="1" stop-color="#94949a"/>
        </linearGradient>
      </defs>
      <path d="M0,290 C300,420 650,560 1050,590 L1050,600 L0,600 Z" fill="var(--brand-blue)"/>
      <path d="M0,312 C300,440 650,574 1050,600 L0,600 Z" fill="var(--card-white)"/>
      <path d="M0,322 C300,450 650,582 1050,608 L0,608 Z" fill="url(#waveGrey)"/>
    </svg>

    <section class="card-content">
      <h1 class="brand-name">Veralink</h1>
      <p class="person-name">Employee Name</p>
      <p class="person-title">Managing Director</p>
      <ul class="contact-list">
        <li class="contact-item">000.000.0000
          <svg class="contact-icon" viewBox="0 0 28 28" aria-hidden="true"><rect width="28" height="28" fill="var(--brand-blue)"/><path d="M9,7 l3,0 l1.5,4 l-2,1.5 c1,2 2.5,3.5 4.5,4.5 l1.5,-2 l4,1.5 l0,3 c-7,1 -13,-5 -12.5,-12.5 z" fill="#fff"/></svg>
        </li>
        <li class="contact-item">info@youremail.com
          <svg class="contact-icon" viewBox="0 0 28 28" aria-hidden="true"><rect width="28" height="28" fill="var(--brand-blue)"/><rect x="6" y="9" width="16" height="11" fill="none" stroke="#fff" stroke-width="1.8"/><path d="M6,9 L14,15 L22,9" fill="none" stroke="#fff" stroke-width="1.8"/></svg>
        </li>
        <li class="contact-item">www.yourwebsite.com
          <svg class="contact-icon" viewBox="0 0 28 28" aria-hidden="true"><rect width="28" height="28" fill="var(--brand-blue)"/><g fill="none" stroke="#fff" stroke-width="1.6"><circle cx="14" cy="14" r="8"/><ellipse cx="14" cy="14" rx="3.5" ry="8"/><path d="M6,14 H22 M7.5,10 H20.5 M7.5,18 H20.5"/></g></svg>
        </li>
        <li class="contact-item">your address Rd., Suite 000, USA
          <svg class="contact-icon" viewBox="0 0 28 28" aria-hidden="true"><rect width="28" height="28" fill="var(--brand-blue)"/><path d="M14,22 C10,17 8.5,14.5 8.5,12 a5.5,5.5 0 0 1 11,0 c0,2.5 -1.5,5 -5.5,10 z" fill="#fff"/><circle cx="14" cy="12" r="2" fill="var(--brand-blue)"/></svg>
        </li>
      </ul>
    </section>
  </main>
</body>
</html>
```